Property lawyer needs a website for new law firm Sydney

WHO AM I ?
I am a real estate development lawyer based in suburban Sydney Australia with over 14 years experience and have recently started my own law firm "Tallowbrook Legal". The firm is just me (a female) at this stage. I need a website designed that is capable of being edited by me frequently (hoping this is easily done?!) and can be published with the domain name I own - www.tallowbrooklegal.com.au.
My areas of practice are:
* Property development (strata & community titling, due diligence, easements, by-laws and management statements, structuring etc)
* Conveyancing (sale and purchase of residential, commercial and retail property)
* General property law (caveats, transfers, related party transactions, easements, leases, powers of attorney etc).
WEBSITE REQUIREMENTS
I would like a website which conveys professionalism, has a fresh modern corporate look and is easy to navigate. The website will mostly be accessed by potential clients looking for information about me, my areas of practice and how to get in contact with me. My potential clients are corporate developers and individuals who are buying and selling property.
My logo for Tallowbrook Legal (see attached) is simple, clean and professional looking. I would like the website to work with the logo without being too dark.
I haven't written all of the content yet, so please use filler text for everything and structure the menus as described above. The site will need to be capable of being updated and edited by me.
Other than that I will leave the design up to you.
Thanks and happy designing!
Target Market(s)
Professional developers and individuals buying and selling real estate
Industry/Entity Type
Real Estate
Coding
Coded - Design and coding required
Number of Pages Required
4 page
Requirements
Must have
- I would like a website which conveys professionalism, has a fresh modern corporate look and is easy to navigate. The website will mostly be accessed by potential clients looking for information about me, my areas of practice and how to get in contact with me. My potential clients are corporate developers and individuals who are buying and selling property.
- Please use my logo for Tallowbrook Legal. I would like the website to work with the logo - the colours are a dark blue (C 100% M 50% B 50%) and grey (C10% B 40%). I don't want the website to be too dark though.
- I am thinking 4 pages. I would like links across the top of the page for "Practice Areas", "About us" and "Contact us" - these should lead to separate landing pages with the content to be inserted later.
- The contact page should contain space for a potential client to send an email enquiry to the following email address "enquiries@tallowbrooklegal.com.au". My contact details are set out in the attached letterhead (see attached).
- I would also like the home page to set out what my three Practice Areas are - Property Development; Conveyancing; General Property Law. Each area should have some filler text under it which will be completed later and a link to be able to take me to the "Practice Areas" page where more detail on each will be provided.
- Please select images that are relevant to my practice as a property lawyer. The photos you use will be the ones which I use so please choose wisely.
- I will need a link on the bottom of the home page showing that I am a member of "The Counsel Guild of NSW" (see attached logo).
- The bottom of each page should also include the following statement "Tallowbrook Legal is a business name of Tallowbrook Legal Pty Limited ACN 482 517 306, an incorporated legal practice regulated by the Legal Profession Act 2004. Liability limited by a scheme approved under the Professional Standards Legislation."
Nice to have
- Have attached an image of me (not the best) but at least its me. Consider whether to use on "About us" page
Should not have
- No images of gavels, scales of justice or law books.
- Images not to be too masculine
- Website not to be too dark

```html
<!DOCTYPE html>
<html lang="en">
<head>
<meta charset="utf-8">
<title>Tallowbrook Legal — Home</title>
<link rel="stylesheet" href="https://fonts.googleapis.com/css2?family=Playfair+Display:wght@900&family=Arimo:wght@400;700&family=Signika:wght@600&display=swap">
<style>
  :root {
    --page-bg: #ebebea;
    --page-bg-light: #f3f3f2;
    --brand-navy: #0f3d6b;
    --nav-active: #2b307c;
    --nav-active-edge: #1a1e5c;
    --nav-text: #6a6a6a;
    --rule: #d2d2d2;
    --panel: #ffffff;
    --panel-edge: #dcdcdc;
    --band-top: #8493f4;
    --band-bottom: #5b63cb;
    --band-edge: #3a41a3;
    --band-tail: #2a2f8e;
    --social: #0b1038;
    --footer-link: #c4a27c;
    --copyright: #9a9a9a;
    --body-text: #111111;
    --muted-text: #555555;
    --photo-sky: #b9c7d8;
    --photo-ground: #7e8ea3;
  }
  * { box-sizing: border-box; margin: 0; padding: 0; }
  html, body { width: 1200px; height: 553px; overflow: hidden; }
  body {
    position: relative;
    background:
      radial-gradient(ellipse at 40% 10%, var(--page-bg-light), transparent 60%),
      radial-gradient(ellipse at 80% 70%, #e6e6e5, transparent 55%),
      var(--page-bg);
    font-family: "Arimo", Arial, sans-serif;
  }
  .brand {
    position: absolute;
    font-family: "Playfair Display", Georgia, serif;
    font-weight: 900;
    color: var(--brand-navy);
    text-transform: uppercase;
    letter-spacing: 0.2px;
    white-space: nowrap;
  }
  .site-header .brand { left: 176px; top: 38px; font-size: 20px; }
  .main-nav a {
    position: absolute;
    top: 40px;
    height: 26px;
    line-height: 26px;
    text-decoration: none;
    font-family: "Signika", Verdana, sans-serif;
    font-weight: 600;
    font-size: 13px;
    color: var(--nav-text);
  }
  .main-nav a.is-active {
    left: 609px; width: 100px;
    text-align: center;
    background: linear-gradient(#343a8c, var(--nav-active));
    border: 1px solid var(--nav-active-edge);
    border-radius: 8px;
    color: #fff;
    font-family: "Arimo", Arial, sans-serif;
    font-weight: 400;
    font-size: 15px;
  }
  .header-rule {
    position: absolute; left: 176px; top: 102px; width: 843px; height: 1px;
    background: var(--rule);
    box-shadow: 0 1px 0 #fafafa;
  }

  .content-panel {
    position: absolute; left: 198px; top: 136px; width: 799px; height: 360px;
    background: var(--panel);
    border: 1px solid var(--panel-edge);
    border-radius: 4px;
    box-shadow: 0 6px 6px -4px rgba(0,0,0,0.18);
  }
  .intro {
    position: absolute; left: 13px; top: 22px; width: 770px;
    font-size: 12.5px; line-height: 16px; color: var(--body-text);
  }
  .practice-areas {
    position: absolute; left: 13px; top: 52px; width: 771px;
    display: flex; gap: 18px;
  }
  .practice-card { width: 245px; }
  .practice-photo {
    height: 74px; border-radius: 3px;
    background: linear-gradient(var(--photo-sky), var(--photo-ground));
  }
  .practice-card h2 {
    margin-top: 9px;
    font-size: 12.5px; font-weight: 700; color: var(--brand-navy);
  }
  .practice-card p {
    margin-top: 4px;
    font-size: 11px; line-height: 14px; color: var(--muted-text);
  }
  .practice-card a {
    display: inline-block; margin-top: 5px;
    font-size: 11px; color: var(--nav-active); text-decoration: none;
  }

  .footer-tails { position: absolute; left: 181px; top: 440px; }
  .footer-band {
    position: absolute; left: 181px; top: 386px; width: 832px; height: 57px;
    background: linear-gradient(var(--band-top), var(--band-bottom));
    border: 1px solid var(--band-edge);
    border-radius: 4px;
    box-shadow: inset 0 1px 0 rgba(255,255,255,0.35);
  }
  .footer-band .brand { left: 21px; top: 17px; font-size: 15px; }
  .social-links { position: absolute; top: 16px; left: 0; }
  .social-links a {
    position: absolute; top: 0; width: 22px; height: 22px;
    background: var(--social);
    display: block;
  }
  .footer-nav {
    position: absolute; left: 0; width: 1200px; top: 462px;
    text-align: center; font-size: 8.5px; color: var(--footer-link);
  }
  .footer-nav a { color: var(--footer-link); text-decoration: none; }
  .footer-nav span { margin: 0 9px; color: #b9b0a5; }
  .guild-link {
    position: absolute; left: 0; width: 1200px; top: 478px;
    display: flex; justify-content: center; align-items: center; gap: 5px;
    font-size: 8.5px; color: var(--nav-text); text-decoration: none;
  }
  .guild-badge { width: 9px; height: 9px; background: var(--brand-navy); }
  .copyright {
    position: absolute; left: 0; width: 1200px; top: 508px;
    text-align: center; font-size: 8.5px; color: var(--copyright);
  }
  .legal-statement {
    position: absolute; left: 250px; width: 700px; top: 524px;
    text-align: center; font-size: 8px; line-height: 11px; color: var(--copyright);
  }
</style>
</head>
<body>
  <header class="site-header">
    <div class="brand">Tallowbrook Legal</div>
    <nav class="main-nav">
      <a class="is-active" href="#">Home</a>
      <a href="#" style="left:741px">About</a>
      <a href="#" style="left:837px">Contact</a>
      <a href="#" style="left:926px">Prac. Areas</a>
    </nav>
    <div class="header-rule"></div>
  </header>

  <main class="content-panel">
    <p class="intro">Real estate development lawyer in suburban Sydney with over 14 years' experience, helping developers, buyers and sellers.</p>
    <section class="practice-areas">
      <article class="practice-card">
        <div class="practice-photo" role="img" aria-label="Photo of a new residential development under construction"></div>
        <h2>Property Development</h2>
        <p>Strata and community titling, due diligence, easements, by-laws and structuring advice.</p>
        <a href="#">Read more &rarr;</a>
      </article>
      <article class="practice-card">
        <div class="practice-photo" role="img" aria-label="Photo of a suburban home with a sold sign"></div>
        <h2>Conveyancing</h2>
        <p>Sale and purchase of residential, commercial and retail property, handled with care.</p>
        <a href="#">Read more &rarr;</a>
      </article>
      <article class="practice-card">
        <div class="practice-photo" role="img" aria-label="Photo of a modern commercial building facade"></div>
        <h2>General Property Law</h2>
        <p>Caveats, transfers, related party transactions, leases and powers of attorney.</p>
        <a href="#">Read more &rarr;</a>
      </article>
    </section>
  </main>

  <svg class="footer-tails" width="832" height="14" viewBox="0 0 832 14" aria-hidden="true">
    <path d="M0 0 H17 V13 Q4 12 0 0 Z" fill="var(--band-tail)"/>
    <path d="M832 0 H815 V13 Q828 12 832 0 Z" fill="var(--band-tail)"/>
  </svg>

  <footer class="footer-band">
    <div class="brand">Tallowbrook Legal</div>
    <div class="social-links">
      <a href="#" aria-label="Social profile one" style="left:687px"></a>
      <a href="#" aria-label="Social profile two" style="left:731px"></a>
      <a href="#" aria-label="Social profile three" style="left:778px"></a>
    </div>
  </footer>

  <nav class="footer-nav">
    <a href="#">Home</a><span>|</span><a href="#">About</a><span>|</span><a href="#">Contact</a><span>|</span><a href="#">Prac. Areas</a>
  </nav>
  <a class="guild-link" href="#"><span class="guild-badge"></span>Member of The Counsel Guild of NSW</a>
  <p class="copyright">© Copyright © 2015 TALLOWBROOK LEGAL all rights reserved</p>
  <p class="legal-statement">Tallowbrook Legal is a business name of Tallowbrook Legal Pty Limited ACN 482 517 306, an incorporated legal practice regulated by the Legal Profession Act 2004. Liability limited by a scheme approved under the Professional Standards Legislation.</p>
</body>
</html>
```